Business Card Design

We need a business card for a new business based in Sydney, Australia. It is a home based baking business, the key products are cookies and muffins and slices including gluten free baked goods. With the emphasis on home made baking. The target market is cafes, coffee shops and vans, restaurants. Products may be provided in display jars or individually wrapped. The final design should be in the colours pink, purple.

Business

Tindle's Bakery Pty Ltd, Marisa Pellow, marisa@tindlesbakery.com.au
0451 276 308, www.tindlesbakery.com.au, ACN 512 648 397,

```html
<!DOCTYPE html>
<html lang="en">
<head>
<meta charset="utf-8">
<title>Tindle's Bakery – Business Card</title>
<link rel="stylesheet" href="https://fonts.googleapis.com/css2?family=Berkshire+Swash&family=Open+Sans:wght@400;600&display=swap">
<style>
  :root {
    --page-bg: #2b2b2b;
    --pink-light: #f48cc4;
    --pink-mid: #ea5fa8;
    --band-pink: #fbc6e3;
    --badge-pink: #c8479f;
    --purple: #7a1485;
    --purple-deep: #5c0c68;
    --ink-purple: #5a0f6e;
    --white: #ffffff;
  }
  * { box-sizing: border-box; margin: 0; padding: 0; }
  html, body {
    width: 1200px;
    height: 1037px;
    overflow: hidden;
    background: var(--page-bg);
  }
  .stage {
    position: relative;
    width: 1200px;
    height: 1037px;
    display: flex;
    align-items: center;
    justify-content: center;
  }
  .card {
    position: relative;
    width: 960px;
    height: 548px;
    overflow: hidden;
    box-shadow: 0 18px 40px rgba(0, 0, 0, 0.5);
    background: linear-gradient(180deg, var(--purple) 0%, var(--purple-deep) 100%);
    font-family: "Open Sans", sans-serif;
  }
  .card__pattern {
    position: absolute;
    left: 0; top: 0;
    width: 100%;
    height: 206px;
    background: linear-gradient(135deg, var(--pink-light) 0%, var(--pink-mid) 100%);
  }
  .card__band {
    position: absolute;
    left: 0; top: 206px;
    width: 100%;
    height: 56px;
    background: var(--band-pink);
    box-shadow: 0 3px 6px rgba(60, 0, 60, 0.25);
  }
  .brand {
    position: absolute;
    left: 70px;
    top: 90px;
    width: 290px;
    height: 290px;
    border-radius: 50%;
    background: var(--badge-pink);
    box-shadow: 0 6px 14px rgba(50, 0, 50, 0.35);
    display: flex;
    align-items: center;
    justify-content: center;
  }
  .brand__name {
    font-family: "Open Sans", sans-serif;
    font-weight: 600;
    font-size: 36px;
    line-height: 1.15;
    color: var(--white);
    text-align: center;
  }
  .holder-name {
    position: absolute;
    left: 440px;
    top: 206px;
    height: 56px;
    display: flex;
    align-items: center;
    font-family: "Berkshire Swash", cursive;
    font-weight: 400;
    font-size: 30px;
    color: var(--ink-purple);
    letter-spacing: 0.5px;
  }
  .contacts {
    position: absolute;
    left: 446px;
    top: 284px;
    list-style: none;
    color: var(--white);
    font-size: 20px;
  }
  .contacts__item {
    display: flex;
    align-items: center;
    height: 40px;
  }
  .contacts__icon {
    width: 20px;
    height: 20px;
    margin-right: 20px;
    flex: none;
  }
  .contacts__item--plain { padding-left: 40px; }
</style>
</head>
<body>
<main class="stage">
  <article class="card">
    <div class="card__pattern" role="img" aria-label="Diagonal pink stripe pattern"></div>
    <div class="card__band"></div>

    <div class="brand">
      <p class="brand__name">Tindle's<br>Bakery<br>Pty Ltd</p>
    </div>

    <h1 class="holder-name">Marisa Pellow</h1>

    <ul class="contacts">
      <li class="contacts__item">
        <svg class="contacts__icon" viewBox="0 0 24 24" aria-hidden="true">
          <path fill="#fff" d="M6.6 10.8a15.1 15.1 0 0 0 6.6 6.6l2.2-2.2c.3-.3.7-.4 1-.2 1.1.4 2.3.6 3.6.6.6 0 1 .4 1 1V20c0 .6-.4 1-1 1C10.6 21 3 13.4 3 4c0-.6.4-1 1-1h3.5c.6 0 1 .4 1 1 0 1.3.2 2.5.6 3.6.1.3 0 .7-.2 1z"/>
        </svg>
        <span>0451 276 308</span>
      </li>
      <li class="contacts__item">
        <svg class="contacts__icon" viewBox="0 0 24 24" aria-hidden="true">
          <rect x="2" y="5" width="20" height="14" rx="1.5" fill="none" stroke="#fff" stroke-width="2"/>
          <path d="M3 6l9 7 9-7" fill="none" stroke="#fff" stroke-width="2"/>
        </svg>
        <span>marisa@tindlesbakery.com.au</span>
      </li>
      <li class="contacts__item">
        <svg class="contacts__icon" viewBox="0 0 24 24" aria-hidden="true">
          <g fill="none" stroke="#fff" stroke-width="1.8">
            <circle cx="12" cy="12" r="9.5"/>
            <ellipse cx="12" cy="12" rx="4.2" ry="9.5"/>
            <path d="M2.5 12h19M4 7h16M4 17h16"/>
          </g>
        </svg>
        <span>www.tindlesbakery.com.au</span>
      </li>
      <li class="contacts__item contacts__item--plain">
        <span>ACN 512 648 397</span>
      </li>
    </ul>
  </article>
</main>
</body>
</html>
```